Business Card

We need some ideas for corporate business cards. I'm interested in a double sided card, with one side featuring our corporate logo, the other side with employee information.

Corporate colors, logo etc. available at www.brivalo.com

Industry/Entity Type

Business

Requirements
Must have
• The "Brivalo" logo with stylized "O"

Nice to have
• Preferred font is calibri

```html
<!DOCTYPE html>
<html lang="en">
<head>
<meta charset="utf-8">
<title>Brivalo Business Card</title>
<link rel="stylesheet" href="https://fonts.googleapis.com/css2?family=Michroma&family=Roboto+Condensed:wght@400&display=swap">
<style>
  :root {
    --backdrop: #acadaf;
    --brand-blue: #46629a;
    --brand-blue-light: #4b6ba4;
    --paper: #ffffff;
    --lavender: #e4e4ef;
    --ink: #111111;
    --icon-blue: #5aa6d9;
    --shadow: rgba(0,0,0,0.45);
  }
  html, body {
    margin: 0;
    padding: 0;
    width: 1017px;
    height: 1200px;
    overflow: hidden;
    background: var(--backdrop);
  }
  .canvas {
    position: relative;
    width: 1017px;
    height: 1200px;
  }
  .card {
    position: absolute;
    left: 152px;
    width: 724px;
    height: 402px;
    overflow: hidden;
    box-shadow: 8px 8px 8px var(--shadow);
  }
  .card--front { top: 149px; background: var(--brand-blue); }
  .card--back { top: 659px; background: var(--paper); }

  .band { position: absolute; }
  .front-side-band { left: 660px; top: 0; width: 64px; height: 402px; background: var(--brand-blue-light); }
  .front-base-band { left: 264px; top: 352px; width: 396px; height: 50px; background: var(--brand-blue-light); }
  .front-rise-band { left: 90px; top: 120px; width: 60px; height: 282px; background: var(--brand-blue-light); opacity: .7; }

  .wordmark {
    position: absolute;
    font-family: "Michroma", sans-serif;
    font-weight: 400;
    color: var(--paper);
    letter-spacing: 4px;
    white-space: nowrap;
  }
  .front-wordmark { left: 275px; top: 268px; font-size: 58px; line-height: 1; }

  .back-ribbon { position: absolute; left: 0; top: 48px; }
  .back-wordmark { left: 48px; top: 64px; font-size: 44px; line-height: 1; }
  .back-drop-band { left: 344px; top: 130px; width: 54px; height: 222px; background: var(--lavender); }
  .back-base-band { left: 121px; top: 292px; width: 277px; height: 60px; background: var(--lavender); }
  .back-rise-band { left: 60px; top: 190px; width: 61px; height: 162px; background: var(--lavender); }

  .holder-name {
    position: absolute;
    right: 42px;
    top: 238px;
    margin: 0;
    font-family: "Michroma", sans-serif;
    font-weight: 400;
    font-size: 27px;
    letter-spacing: 1px;
    color: var(--ink);
  }
  .contact {
    position: absolute;
    right: 42px;
    top: 292px;
    margin: 0;
    padding: 0;
    list-style: none;
    font-family: "Roboto Condensed", sans-serif;
    font-size: 17px;
    color: var(--ink);
    text-align: right;
  }
  .contact li { height: 23px; line-height: 23px; }
  .contact-item { white-space: nowrap; margin-left: 10px; }
  .icon { display: inline-block; vertical-align: -3px; margin-left: 5px; }
</style>
</head>
<body>
<main class="canvas">

  <section class="card card--front" aria-label="Card front">
    <div class="band front-rise-band"></div>
    <div class="band front-base-band"></div>
    <div class="band front-side-band"></div>
    <div class="wordmark front-wordmark">BRIVALO</div>
  </section>

  <section class="card card--back" aria-label="Card back">
    <div class="band back-rise-band"></div>
    <div class="band back-base-band"></div>
    <div class="band back-drop-band"></div>
    <svg class="back-ribbon" width="400" height="82" viewBox="0 0 400 82" aria-hidden="true">
      <polygon points="0,0 374,0 398,41 374,82 0,82" fill="var(--brand-blue)"/>
    </svg>
    <div class="wordmark back-wordmark">BRIVALO</div>

    <h1 class="holder-name">Ciaran Dunleavy</h1>

    <ul class="contact">
      <li>
        <span class="contact-item">14 Harbour Lane, Riverside Business Park, Dublin 8, Ireland</span><svg class="icon" width="17" height="17" viewBox="0 0 17 17" aria-label="Address"><rect width="17" height="17" rx="3" fill="var(--icon-blue)"/><path d="M8.5 3a3.3 3.3 0 0 0-3.3 3.3c0 2.5 3.3 7 3.3 7s3.3-4.5 3.3-7A3.3 3.3 0 0 0 8.5 3z" fill="#fff"/><circle cx="8.5" cy="6.3" r="1.2" fill="var(--icon-blue)"/></svg>
      </li>
      <li>
        <span class="contact-item">+353 1 555 0142</span><svg class="icon" width="17" height="17" viewBox="0 0 17 17" aria-label="Phone"><rect width="17" height="17" rx="3" fill="var(--icon-blue)"/><path d="M4.5 4c1-.6 1.6-.3 2 .6l.6 1.4c.2.5 0 .9-.4 1.2l-.6.4c.6 1.3 1.5 2.2 2.8 2.8l.4-.6c.3-.4.7-.6 1.2-.4l1.4.6c.9.4 1.2 1 .6 2-1.5 1.8-4 .6-6-1.4S2.7 5.5 4.5 4z" fill="#fff"/></svg>
        <span class="contact-item">+353 1 555 0143</span><svg class="icon" width="17" height="17" viewBox="0 0 17 17" aria-label="Mobile"><rect width="17" height="17" rx="3" fill="var(--icon-blue)"/><rect x="5.5" y="3" width="6" height="11" rx="1.2" fill="#fff"/><rect x="6.5" y="4.5" width="4" height="7" fill="var(--icon-blue)"/></svg>
      </li>
      <li>
        <span class="contact-item">www.brivalo.com</span><svg class="icon" width="17" height="17" viewBox="0 0 17 17" aria-label="Website"><rect width="17" height="17" rx="3" fill="var(--icon-blue)"/><circle cx="8.5" cy="8.5" r="5" fill="none" stroke="#fff" stroke-width="1.2"/><ellipse cx="8.5" cy="8.5" rx="2" ry="5" fill="none" stroke="#fff" stroke-width="1"/><line x1="3.5" y1="8.5" x2="13.5" y2="8.5" stroke="#fff" stroke-width="1"/></svg>
        <span class="contact-item">info@brivalo.com</span><svg class="icon" width="17" height="17" viewBox="0 0 17 17" aria-label="Email"><rect width="17" height="17" rx="3" fill="var(--icon-blue)"/><rect x="3" y="5" width="11" height="7.5" rx="1" fill="#fff"/><path d="M3.5 5.5l5 3.8 5-3.8" fill="none" stroke="var(--icon-blue)" stroke-width="1"/></svg>
      </li>
    </ul>
  </section>

</main>
</body>
</html>
```